Professional individual needs business card design

I need a business card designed for my friend to show their skills and contact details

I would like to see pattern designs with a black foreground and strong look - will submit content specifics but basics are:

NAME SURNAME (large and bold)
Event Manager & MC

Velvet Harbour
The other event I run

phone number - email

```html
<!DOCTYPE html>
<html lang="en">
<head>
<meta charset="utf-8">
<title>Leo Marsh – Business Card</title>
<link rel="stylesheet" href="https://fonts.googleapis.com/css2?family=Righteous&family=Questrial&display=swap">
<style>
  :root {
    --page-bg: #e7e4df;
    --card-top: #232226;
    --card-bottom: #0e0e11;
    --ink: #ffffff;
    --ink-soft: #e6e6e8;
  }
  * { box-sizing: border-box; margin: 0; padding: 0; }
  html, body {
    width: 1200px;
    height: 972px;
    overflow: hidden;
    background: var(--page-bg);
  }
  .stage {
    position: relative;
    width: 1200px;
    height: 972px;
    display: flex;
    align-items: center;
    justify-content: center;
  }
  .card {
    position: relative;
    width: 840px;
    height: 480px;
    border-radius: 4px;
    overflow: hidden;
    color: var(--ink);
  }
  .card__pattern {
    position: absolute;
    inset: 0;
    background: linear-gradient(160deg, var(--card-top) 0%, var(--card-bottom) 100%);
  }
  .card__content {
    position: relative;
    height: 100%;
    display: flex;
    flex-direction: column;
    align-items: center;
    padding-top: 92px;
  }
  .card__name {
    font-family: "Righteous", sans-serif;
    font-size: 56px;
    letter-spacing: 1px;
    line-height: 1;
  }
  .card__role {
    font-family: "Questrial", sans-serif;
    font-size: 25px;
    color: var(--ink-soft);
    letter-spacing: 1px;
    margin-top: 14px;
  }
  .card__venture {
    font-family: "Questrial", sans-serif;
    text-align: center;
    color: var(--ink-soft);
    margin-top: 30px;
    line-height: 1.2;
  }
  .card__venture-name { font-size: 25px; letter-spacing: 1px; }
  .card__venture-note { font-size: 23px; letter-spacing: 0.5px; }
  .contact {
    list-style: none;
    align-self: flex-start;
    margin-left: 262px;
    margin-top: 34px;
    display: flex;
    flex-direction: column;
    gap: 14px;
  }
  .contact__item {
    display: flex;
    align-items: center;
    gap: 16px;
    font-family: "Questrial", sans-serif;
  }
  .contact__icon { width: 34px; height: 34px; flex: none; }
  .contact__phone { font-size: 21px; letter-spacing: 1px; }
  .contact__email { font-size: 17px; font-weight: 700; letter-spacing: 0.5px; }
</style>
</head>
<body>
<main class="stage">
  <article class="card">
    <div class="card__pattern" role="img" aria-label="Fine diagonal criss-cross line pattern on a black background"></div>
    <div class="card__content">
      <h1 class="card__name">Leo Marsh</h1>
      <p class="card__role">Event Manager &amp; MC</p>
      <div class="card__venture">
        <p class="card__venture-name">Velvet Harbour</p>
        <p class="card__venture-note">The other event I run</p>
      </div>
      <ul class="contact">
        <li class="contact__item">
          <svg class="contact__icon" viewBox="0 0 34 34" aria-hidden="true">
            <circle cx="17" cy="17" r="15.5" fill="none" stroke="var(--ink)" stroke-width="1.6"/>
            <path d="M12.5 9.5c1-.6 2-.3 2.5.6l1.3 2.4c.4.8.2 1.7-.5 2.2l-1 .7c.8 2 2.2 3.6 4 4.6l.8-.9c.6-.6 1.5-.7 2.2-.2l2.2 1.5c.8.6 1 1.6.4 2.5l-.7 1c-.9 1.2-2.5 1.6-3.9 1-4.5-2-7.9-5.9-9.2-10.6-.4-1.4.1-2.9 1.3-3.8z" fill="var(--ink)"/>
          </svg>
          <span class="contact__phone">555.014.2390</span>
        </li>
        <li class="contact__item">
          <svg class="contact__icon" viewBox="0 0 34 34" aria-hidden="true">
            <circle cx="17" cy="17" r="15.5" fill="none" stroke="var(--ink)" stroke-width="1.6"/>
            <rect x="9" y="11.5" width="16" height="11" fill="none" stroke="var(--ink)" stroke-width="1.5"/>
            <path d="M9 11.5l8 6.5 8-6.5" fill="none" stroke="var(--ink)" stroke-width="1.5"/>
          </svg>
          <span class="contact__email">LeoMarsh@VelvetHarbour.com</span>
        </li>
      </ul>
    </div>
  </article>
</main>
</body>
</html>
```